Vintage soap dispenser label

I'm making a series of glass bottle soap dispensers (soap, lotion, shampoo, etc.). I really love a competitor's design, but I don't want to copy it. I'm interested in the clean, urban vintage style. There can be a lot of filler text as in their design which fills the negative space, but note that the buyer will fill the bottles with their own products, so things like "100% Natural Ingredients" and the like are somewhat bogus. Because they are to be refillable, reusable bottles, some text to that effect may be more appropriate, plus our company name "Velmora Home", and perhaps the style of the bottle "Boston Round" and other text like the size of the bottle. I need a basic design, 3.25" wide x 3.5" tall and I will adjust the text as necessary for the various products my buyers will use. My competitor that is very similar to my business is https://shoplink.example/7KpR2vX. As you can see, they have a signature style. I'd like my own signature style. (I plan to have a vintage line and a contemporary line of products, so I'll likely be posting a second request for that.)

Requirements
Should not have
• Not too ornate. Should be somewhat minimalistic

```html
<!DOCTYPE html>
<html lang="en">
<head>
<meta charset="utf-8">
<title>Velmora Home – Refillable Bottle Labels</title>
<link rel="stylesheet" href="https://fonts.googleapis.com/css2?family=Oswald:wght@400&family=Montserrat:wght@400;600&display=swap">
<style>
  :root {
    --ink: #1f1b1a;
    --paper: #ffffff;
    --canvas-edge: #cfcfcf;
    --label-edge: #9a9a9a;
  }
  * { box-sizing: border-box; margin: 0; padding: 0; }
  html, body { width: 1200px; height: 999px; overflow: hidden; background: var(--paper); }
  .canvas {
    position: relative; width: 1200px; height: 999px;
    border: 1px solid var(--canvas-edge);
    font-family: "Montserrat", Arial, sans-serif;
  }
  .label {
    position: absolute; left: 58px; width: 390px; height: 420px;
    text-align: center;
  }
  .label--dark { top: 60px; background: var(--ink); color: var(--paper); }
  .label--light { top: 523px; background: var(--paper); color: var(--ink); outline: 1px solid var(--label-edge); }
  .label__frame { position: absolute; inset: 0; width: 100%; height: 100%; }
  .label__frame line { stroke: currentColor; stroke-width: 2; }
  .label__text { position: absolute; left: 0; right: 0; }
  .brand {
    top: 43px; display: inline-block; left: 50%; right: auto; transform: translateX(-50%);
    padding: 4px 8px; font-weight: 600; font-size: 17px; letter-spacing: .2px; border-radius: 3px;
  }
  .label--dark .brand { background: var(--paper); color: var(--ink); }
  .label--light .brand { background: var(--ink); color: var(--paper); }
  .product {
    top: 148px; font-family: "Oswald", "Arial Narrow", sans-serif; font-weight: 400;
    font-size: 70px; line-height: 1; letter-spacing: 1px; transform: scaleX(.88);
  }
  .note { top: 260px; font-size: 13px; }
  .tagline { top: 323px; font-size: 14px; }
  .volume { top: 368px; font-size: 14px; }
</style>
</head>
<body>
<main class="canvas">

  <section class="label label--dark" aria-label="Hand soap label">
    <svg class="label__frame" viewBox="0 0 390 420" aria-hidden="true">
      <line x1="8" y1="10" x2="382" y2="10"/><line x1="12" y1="4" x2="12" y2="16"/><line x1="378" y1="4" x2="378" y2="16"/>
      <line x1="30" y1="18" x2="360" y2="18"/>
      <line x1="8" y1="410" x2="382" y2="410"/><line x1="12" y1="404" x2="12" y2="416"/><line x1="378" y1="404" x2="378" y2="416"/>
      <line x1="30" y1="402" x2="360" y2="402"/>
      <line x1="20" y1="6" x2="20" y2="414"/><line x1="370" y1="6" x2="370" y2="414"/>
      <line x1="30" y1="14" x2="30" y2="406"/><line x1="360" y1="14" x2="360" y2="406"/>
      <line x1="20" y1="103" x2="370" y2="103"/><line x1="20" y1="288" x2="370" y2="288"/>
      <line x1="80" y1="316" x2="310" y2="316"/><line x1="80" y1="310" x2="80" y2="322"/><line x1="310" y1="310" x2="310" y2="322"/>
      <line x1="80" y1="348" x2="310" y2="348"/><line x1="80" y1="342" x2="80" y2="354"/><line x1="310" y1="342" x2="310" y2="354"/>
    </svg>
    <span class="label__text brand">VELMORA HOME</span>
    <h2 class="label__text product">HAND SOAP</h2>
    <p class="label__text note">REFILLABLE BOTTLE</p>
    <p class="label__text tagline">100% NATURAL INGREDIENTS</p>
    <p class="label__text volume">500 ML | 16.91 FL</p>
  </section>

  <section class="label label--light" aria-label="Shampoo label">
    <svg class="label__frame" viewBox="0 0 390 420" aria-hidden="true">
      <line x1="8" y1="18" x2="382" y2="18"/><line x1="12" y1="12" x2="12" y2="24"/><line x1="378" y1="12" x2="378" y2="24"/>
      <line x1="30" y1="10" x2="360" y2="10"/>
      <line x1="8" y1="404" x2="382" y2="404"/><line x1="12" y1="398" x2="12" y2="410"/><line x1="378" y1="398" x2="378" y2="410"/>
      <line x1="30" y1="412" x2="360" y2="412"/>
      <line x1="20" y1="14" x2="20" y2="408"/><line x1="370" y1="14" x2="370" y2="408"/>
      <line x1="30" y1="6" x2="30" y2="416"/><line x1="360" y1="6" x2="360" y2="416"/>
      <line x1="20" y1="105" x2="370" y2="105"/><line x1="20" y1="288" x2="370" y2="288"/>
      <line x1="80" y1="316" x2="310" y2="316"/><line x1="80" y1="310" x2="80" y2="322"/><line x1="310" y1="310" x2="310" y2="322"/>
      <line x1="80" y1="348" x2="310" y2="348"/><line x1="80" y1="342" x2="80" y2="354"/><line x1="310" y1="342" x2="310" y2="354"/>
    </svg>
    <span class="label__text brand">VELMORA HOME</span>
    <h2 class="label__text product">SHAMPOO</h2>
    <p class="label__text note">REFILLABLE BOTTLE</p>
    <p class="label__text tagline">100% NATURAL INGREDIENTS</p>
    <p class="label__text volume">500 ML | 16.91 FL</p>
  </section>

</main>
</body>
</html>
```